Tax Folder

Looking for a professional client tax folder design.
Please also include this on the design:

Mio-Lan Brackwell, EA
Enrolled Agent, KVO Certified ITIN Acceptance Agent

Size: when open both sides: 54 x 41 cm
when it folds half side: 24.5 x 30.5 cm

```html
<!DOCTYPE html>
<html lang="en">
<head>
<meta charset="utf-8">
<title>Brightline Tax Co — Client Tax Folder</title>
<link href="https://fonts.googleapis.com/css2?family=Poppins:wght@400;500;600;700;800&display=swap" rel="stylesheet">
<style>
  :root{
    --navy:#0f1c3f;
    --navy-deep:#0a1530;
    --cyan:#2bb8ea;
    --yellow:#f7c417;
    --yellow-soft:#fde58a;
    --white:#ffffff;
    --stage:#ecebe8;
  }
  *{margin:0;padding:0;box-sizing:border-box}
  html,body{width:804px;height:1200px;overflow:hidden;background:var(--stage);font-family:'Poppins',sans-serif}
  .folder{position:absolute;left:23px;top:328px;width:757px;height:543px}
  .folder-art{position:absolute;inset:0}
  .abs{position:absolute;white-space:nowrap}
  .centered{transform:translateX(-50%);text-align:center}

  .company{display:flex;align-items:center;gap:9px}
  .company-square{width:14px;height:14px;background:var(--navy)}
  .company-name{font-weight:600;font-size:17px;line-height:1;color:var(--navy)}
  .company-front{left:500px;top:32px}
  .company-back{left:552px;top:467px;transform:translate(-50%,-50%) rotate(180deg)}
  .company-back .company-square{background:var(--white)}
  .company-back .company-name{color:var(--white)}

  .headline{left:552px;top:263px;font-weight:800;font-size:26px;line-height:23px;color:var(--cyan)}
  .headline .line-two{color:var(--yellow)}
  .dots{left:552px;top:317px;display:flex;gap:3px;transform:translateX(-50%)}
  .dots span{width:5px;height:4px;background:var(--yellow)}
  .dots span:nth-child(2),.dots span:nth-child(3){background:var(--cyan)}
  .agent-name{left:552px;top:327px;font-weight:700;font-size:13.5px;color:var(--cyan)}
  .agent-name small{font-weight:500;font-size:13.5px}
  .agent-role{left:552px;font-size:10.5px;color:var(--white);line-height:1}
  .role-one{top:345px}
  .role-two{top:358px}
  .web-front{left:552px;top:378px;font-size:9px;letter-spacing:3.4px;color:var(--white);font-weight:500}
  .web-front b{color:var(--yellow);font-weight:700}

  .contact{left:198px;font-size:6.2px;color:var(--white);line-height:1}
  .web-back{left:198px;top:455px;font-size:10px;letter-spacing:1px;color:var(--white);transform:translateX(-50%) rotate(180deg)}
</style>
</head>
<body>
<main class="folder">
  <svg class="folder-art" viewBox="0 0 757 543" width="757" height="543">
    <defs>
      <clipPath id="folder-shape">
        <path d="M0,0 H757 V400 H727 V543 H404 V400 H360 V543 H35 V400 H0 Z"/>
      </clipPath>
      <clipPath id="navy-shape">
        <path d="M0,284 C220,270 470,222 727,142 L757,133 V400 H727 V543 H404 V400 H360 V543 H35 V400 H0 Z"/>
      </clipPath>
      <linearGradient id="photo-tone" x1="0" y1="0" x2="1" y2="1">
        <stop offset="0" stop-color="#d6dde6"/>
        <stop offset=".5" stop-color="#b9c8d8"/>
        <stop offset="1" stop-color="#eef0f2"/>
      </linearGradient>
      <linearGradient id="yellow-band" x1="0" x2="1">
        <stop offset="0" stop-color="#f9d23c"/>
        <stop offset="1" stop-color="#f7c417"/>
      </linearGradient>
    </defs>

    <g clip-path="url(#folder-shape)">
      <rect class="paper" width="757" height="543" fill="var(--white)"/>
      <circle class="faint-circle" cx="198" cy="136" r="87" fill="var(--yellow-soft)" opacity=".45"/>

      <g clip-path="url(#navy-shape)">
        <rect class="navy-field" width="757" height="543" fill="var(--navy)"/>
        <g class="chart-bars" fill="#1b2b55" opacity=".6">
          <rect x="20" y="360" width="12" height="60"/><rect x="60" y="340" width="12" height="80"/>
          <rect x="100" y="365" width="12" height="55"/><rect x="140" y="330" width="12" height="90"/>
          <rect x="260" y="350" width="12" height="70"/><rect x="300" y="320" width="12" height="100"/>
          <rect x="340" y="345" width="12" height="75"/><rect x="420" y="335" width="12" height="85"/>
          <rect x="460" y="360" width="12" height="60"/><rect x="500" y="325" width="12" height="95"/>
          <rect x="620" y="340" width="12" height="80"/><rect x="660" y="355" width="12" height="65"/>
          <rect x="700" y="330" width="12" height="90"/><rect x="740" y="350" width="12" height="70"/>
        </g>
        <polyline class="chart-line" points="0,300 90,322 180,296 300,330 420,300 530,318 640,290 757,300" fill="none" stroke="#2bb8ea" stroke-width="1" opacity=".3"/>
        <rect class="navy-base" y="455" width="757" height="88" fill="var(--navy-deep)"/>
      </g>

      <path class="swoosh" d="M0,270 C230,256 470,214 690,142 L704,160 C470,232 230,272 0,280 Z" fill="url(#yellow-band)"/>
      <path class="swoosh-arrow" d="M668,118 L747,108 L718,162 Z" fill="var(--yellow)"/>
    </g>

    <circle class="photo-ring" cx="559" cy="162" r="97" fill="var(--yellow)"/>
    <circle cx="559" cy="160" r="89" fill="var(--white)"/>
    <circle class="photo" cx="559" cy="160" r="86" fill="url(#photo-tone)" role="img" aria-label="Photo of colleagues reviewing financial charts at a desk"/>

    <g class="contact-icons" fill="var(--yellow)" stroke="var(--white)" stroke-width="1">
      <circle cx="198" cy="287" r="7.5"/>
      <circle cx="198" cy="316" r="7.5"/>
      <circle cx="198" cy="345" r="7.5"/>
      <circle cx="198" cy="373" r="7.5"/>
    </g>
    <g class="icon-glyphs" fill="none" stroke="var(--white)" stroke-width="1.2">
      <path d="M198,291 C195,287 195,285 195,284 a3,3 0 0 1 6,0 C201,285 201,287 198,291 Z"/>
      <path d="M195,313 q0,6 6,6 l0,-2 l-2,-1 l-1,1 q-2,-1 -2,-3 l1,-1 l-1,-2 Z"/>
      <rect x="194.5" y="342.5" width="7" height="5"/><path d="M194.5,342.5 L198,345.5 L201.5,342.5"/>
      <circle cx="198" cy="373" r="3.5"/><path d="M194.5,373 H201.5 M198,369.5 V376.5"/>
    </g>
  </svg>

  <div class="abs company company-front">
    <div class="company-square"></div>
    <div class="company-name">Brightline Tax Co</div>
  </div>

  <h1 class="abs centered headline">ADDING PACE TO<br><span class="line-two">YOUR BUSINESS</span></h1>
  <div class="abs dots"><span></span><span></span><span></span><span></span></div>
  <p class="abs centered agent-name">MIO-LAN BRACKWELL, <small>EA</small></p>
  <p class="abs centered agent-role role-one">Enrolled Agent</p>
  <p class="abs centered agent-role role-two">KVO Certified ITIN Acceptance Agent</p>
  <p class="abs centered web-front">www.<b>brightlinetaxco</b>.com</p>

  <div class="abs company company-back">
    <div class="company-square"></div>
    <div class="company-name">Brightline Tax Co</div>
  </div>

  <p class="abs centered contact" style="top:299px">2150 Harlow Creek Rd Ste 204, Danford, OH 43990</p>
  <p class="abs centered contact" style="top:328px">(555) 214-7730</p>
  <p class="abs centered contact" style="top:356px">hello@brightlinetaxco.com</p>
  <p class="abs centered contact" style="top:384px;letter-spacing:1.5px">www.brightlinetaxco.com</p>
  <p class="abs web-back">www.brightlinetaxco.com</p>
</main>
</body>
</html>
```